Instagram Posts for a restaurants

We need 5-10 Instagram posts for a restaurant located in Dubai, UAE.

Background about the restaurant:

Forks and Pails is a boutique burgers and comfort food joint located at Dubai, UAE. We started operations in September 2016. The main focus on our food is for it to be simple, original and freshly made. The majority of our orders are take away with fewer people opting for dinning in. We connect with our customers through our Instagram account & our customers rely on it for updates.

The brief

What we are looking for is a vector design (advertisement) for multiple purposes including:

1. announcing that we started delivery
2. a post that we can use multiple times during the year just as a "reminder that we deliver"
3. posts that serve as an advertisement

posts need to be as simple as possible

for reference, our Instagram account is @forksandpails

Industry/Entity Type

Restaurant

Colors
f04a50
ffffff
000000

Requirements
Should not have
• the designs should not have too many colors

```html
<!DOCTYPE html>
<html lang="en">
<head>
<meta charset="utf-8">
<title>Forks and Pails – We Deliver</title>
<link rel="stylesheet" href="https://fonts.googleapis.com/css2?family=Playfair+Display:wght@900&family=Yellowtail&family=Kaushan+Script&family=Montserrat:wght@400&display=block">
<style>
  :root {
    --brand-red: #f04a50;
    --ink: #1c1c1c;
    --ink-soft: #4a4a4a;
    --paper: #ffffff;
    --sketch-light: #f6f2f0;
    --sketch-mid: #e6dcd7;
  }
  html, body {
    margin: 0;
    padding: 0;
    width: 1200px;
    height: 1200px;
    overflow: hidden;
    background: var(--paper);
  }
  .post {
    position: relative;
    width: 1200px;
    height: 1200px;
    background: var(--paper);
    overflow: hidden;
  }
  .burger-art {
    position: absolute;
    left: 167px;
    top: 61px;
    width: 900px;
    height: 706px;
    border-radius: 450px 450px 110px 110px / 300px 300px 90px 90px;
    background: radial-gradient(ellipse at 50% 35%, var(--sketch-light) 0%, var(--sketch-mid) 100%);
  }
  .brand-name {
    position: absolute;
    left: 228px;
    top: 394px;
    width: 805px;
    height: 345px;
    margin: 0;
    display: flex;
    flex-direction: column;
    justify-content: center;
    align-items: center;
    text-align: center;
    font-family: "Playfair Display", Georgia, serif;
    font-weight: 900;
    font-size: 140px;
    line-height: 1.08;
    color: var(--brand-red);
  }
  .tagline {
    position: absolute;
    left: 0;
    top: 778px;
    width: 1200px;
    margin: 0;
    text-align: center;
    font-family: "Yellowtail", "Kaushan Script", "Brush Script MT", cursive;
    font-size: 88px;
    line-height: 1.1;
    color: var(--ink-soft);
    white-space: nowrap;
  }
  .info-list {
    position: absolute;
    left: 279px;
    top: 896px;
    margin: 0;
    padding: 0;
    list-style: none;
    font-family: "Playfair Display", Georgia, serif;
    font-weight: 900;
    font-size: 78px;
    line-height: 86px;
    font-variant-numeric: lining-nums;
    color: var(--ink);
  }
  .info-list li {
    position: relative;
    white-space: nowrap;
  }
  .info-list li::before {
    content: "";
    position: absolute;
    left: 0;
    top: 32px;
    width: 24px;
    height: 24px;
    border-radius: 50%;
    background: var(--ink);
  }
  .info-list .deliver { padding-left: 99px; }
  .info-list .phone { padding-left: 68px; }
  .map-link {
    position: absolute;
    left: 0;
    top: 1102px;
    width: 1200px;
    margin: 0;
    text-align: center;
    font-family: "Montserrat", Arial, sans-serif;
    font-weight: 400;
    font-size: 35px;
    letter-spacing: 3px;
    text-transform: uppercase;
    color: var(--ink);
  }
</style>
</head>
<body>
  <main class="post">
    <div class="burger-art" role="img" aria-label="Hand-sketched burger illustration with sesame bun, patty and lettuce"></div>
    <h1 class="brand-name"><span>Forks and</span><span>Pails</span></h1>
    <p class="tagline">Freshly made Simple. Original</p>
    <ul class="info-list">
      <li class="deliver">WE DELIVER</li>
      <li class="phone">T: 04-5550187</li>
    </ul>
    <p class="map-link">maps.example.com/forkspails</p>
  </main>
</body>
</html>
```